Electrical Contracting Business Website

Require website done for my contracting business.
Partly done one but really dont have time.

You can view the current one at http://tolbran.net.au

You can use any info/styles/photos from the current website

I like the orange color of the logo so id like things to be with that
Unfortunatly being a new business (Sept 2015) I havent got alot of photos . but if you require any for any of the specifics listed in the doc file ill have a look to see what I have.

I am targeting mainly commercial / industrial clients. Which also includes government and mining.

Target Market(s)

People requiring electricians

Industry/Entity Type

Electrician

Coding

Coded - Design and coding required

Number of Pages Required

5+ page

Colors
f37122

Requirements
Must have
• logo with EC Number
• Keep it simple and not to complicated
• Comply with the current html / style sheet standards.
• Desktop/Mobile Version compatability
Nice to have
• additional photos.
• The domestic lifts we install are by vonrim I dont have any photos of them unfortunately.
Should not have
• change colour of logo

```html
<!DOCTYPE html>
<html lang="en">
<head>
<meta charset="utf-8">
<title>Tolbran Engineering – Electrical Services</title>
<link href="https://fonts.googleapis.com/css2?family=Open+Sans:wght@400;600;700&family=Roboto:wght@300;400;500&display=swap" rel="stylesheet">
<style>
:root{
  --orange:#f37122;
  --orange-dark:#d65a12;
  --ink:#2b2b2b;
  --grey:#777;
  --light:#f3f3f3;
  --line:#dedede;
  --footer:#1f2124;
  --footer-text:#b9bcc0;
}
*{box-sizing:border-box;margin:0;padding:0}
html,body{width:1200px;height:2816px;overflow:hidden}
body{font-family:"Open Sans",sans-serif;color:var(--ink);background:#fff;position:relative}
.abs{position:absolute}

/* header */
.site-header{left:0;top:0;width:1200px;height:80px;background:#fff;border-bottom:1px solid var(--line);z-index:2}
.brand{left:40px;top:12px;display:flex;align-items:center;gap:10px}
.brand .dot{width:22px;height:22px;border-radius:50%;background:var(--orange)}
.brand-name{font-weight:700;font-size:30px;line-height:34px;color:var(--orange);letter-spacing:1px}
.brand-ec{font-size:11px;line-height:14px;color:var(--orange);font-weight:600;letter-spacing:1px}
.phone{right:60px;top:8px;font-size:13px;color:var(--orange);font-weight:600;display:flex;align-items:center;gap:6px}
.main-nav{right:60px;top:48px;display:flex}
.main-nav a{font-family:"Roboto",sans-serif;font-size:13px;color:#555;text-decoration:none;padding:0 22px;border-left:1px solid var(--line)}
.main-nav a:first-child{border-left:0}
.nav-mark{left:572px;top:42px;width:8px;height:8px;border-radius:50%;background:var(--orange)}

/* hero */
.hero-photo{left:0;top:80px;width:1200px;height:800px;
  background:
    radial-gradient(ellipse 420px 360px at 960px 560px,rgba(214,176,48,.55),rgba(214,176,48,0) 70%),
    radial-gradient(ellipse 700px 260px at 600px 120px,rgba(255,255,255,.45),rgba(255,255,255,0) 70%),
    linear-gradient(180deg,#d3dce4 0%,#aebbc7 40%,#8d99a4 72%,#6f7a83 100%)}
.hero-tag{left:100px;top:480px;height:50px;padding:0 30px;background:var(--orange);color:#fff;font-size:20px;font-weight:600;line-height:50px}

/* features */
.feature-panel{left:100px;top:760px;width:1000px;height:330px;background:#fff}
.feature{width:200px;text-align:center}
.feature .ring{width:150px;height:150px;margin:0 auto;border-radius:50%;background:var(--orange);display:flex;align-items:center;justify-content:center}
.feature .core{width:116px;height:116px;border-radius:50%;background:#3a3a3a;display:flex;align-items:center;justify-content:center}
.feature h3{font-family:"Roboto",sans-serif;font-weight:400;font-size:20px;line-height:24px;margin-top:14px;color:var(--ink)}
.about h2{font-family:"Roboto",sans-serif;font-weight:400;font-size:24px;text-align:center}
.accent{color:var(--orange)}
.about p{font-size:11px;line-height:18px;color:var(--grey);text-align:center;margin-top:14px}

/* section headings */
.section-title{left:0;width:1200px;text-align:center;font-family:"Roboto",sans-serif;font-weight:400;font-size:28px}
.section-title::after{content:"";display:block;width:60px;height:2px;background:var(--orange);margin:8px auto 0}

/* services */
.service-card{top:1210px;width:326px;height:340px;color:#fff;text-align:center;padding:50px 28px 0}
.service-card.dark{background:linear-gradient(160deg,#3d4248,#23272b)}
.service-card.active{background:linear-gradient(160deg,#f58a45,var(--orange-dark))}
.service-card h3{font-family:"Roboto",sans-serif;font-weight:300;font-size:34px}
.service-card p{font-size:11px;line-height:17px;margin-top:14px;opacity:.9}
.btn{display:inline-block;background:var(--orange);color:#fff;font-size:12px;font-weight:600;padding:8px 18px;margin-top:20px}
.service-card.active .btn{background:var(--ink)}
.slider-arrow{top:1355px;width:20px;height:30px}

/* projects */
.section-sub{left:0;width:1200px;text-align:center;font-size:13px;color:var(--grey)}
.project{background:linear-gradient(160deg,#8e9aa6,#5e6a75)}
.project.feature-tile{background:#141414;color:#fff;text-align:center}
.feature-tile .plus{width:54px;height:54px;border-radius:50%;border:2px solid var(--orange);margin:120px auto 16px;display:flex;align-items:center;justify-content:center}
.feature-tile span{font-size:15px}

/* partners */
.col-title{font-family:"Roboto",sans-serif;font-weight:400;font-size:26px}
.partners p{font-size:11px;line-height:17px;color:var(--grey);margin-top:14px;width:460px}
.partner-badge{width:120px;height:80px;border:2px solid #c7c7c7;border-radius:8px}
.partner-badge.round{border-radius:50%;width:86px;height:86px}
.form-field{left:640px;width:460px;height:42px;border:1px solid var(--line);font-size:12px;color:#999;padding:12px 14px}
.submit{left:640px;top:2388px;width:460px;height:44px;background:var(--orange);color:#fff;text-align:center;font-size:14px;font-weight:600;line-height:44px;border-radius:3px}

/* footer */
.site-footer{left:0;top:2480px;width:1200px;height:296px;background:var(--footer);color:var(--footer-text)}
.foot-col h4{font-family:"Roboto",sans-serif;font-size:15px;font-weight:500;color:#fff;text-transform:uppercase}
.foot-col h4 .accent{color:var(--orange)}
.foot-col ul{list-style:none;margin-top:14px}
.foot-col li{font-size:12px;line-height:24px}
.foot-col .row{display:flex;gap:10px;font-size:12px;line-height:22px;align-items:flex-start}
.map-area{width:290px;height:140px;background:linear-gradient(160deg,#dfe7d8,#c7d5e0);margin-top:16px}
.foot-brand{display:flex;align-items:center;gap:10px}
.foot-brand .dot{width:20px;height:20px;border-radius:50%;background:#fff}
.foot-brand-name{font-weight:700;font-size:28px;line-height:32px;color:#fff;letter-spacing:1px}
.foot-brand-ec{font-size:11px;line-height:14px;color:#fff;font-weight:600;letter-spacing:1px}
.member-badge{width:160px;height:52px;background:#3a3d41;margin-top:26px}
.copyright{left:0;top:2776px;width:1200px;height:40px;background:var(--orange);color:#fff;font-size:12px;line-height:40px;padding-left:100px}
.social{right:100px;top:2784px;display:flex;gap:8px}
.social span{width:24px;height:24px;border-radius:50%;background:#fff;opacity:.9}
</style>
</head>
<body>

<header class="site-header abs">
  <div class="brand abs">
    <span class="dot"></span>
    <div><div class="brand-name">TOLBRAN</div><div class="brand-ec">ENGINEERING · EC 012345</div></div>
  </div>
  <div class="phone abs">
    <svg width="14" height="14" viewBox="0 0 24 24"><path fill="#f37122" d="M6.6 10.8a15 15 0 0 0 6.6 6.6l2.2-2.2c.3-.3.7-.4 1-.2 1.1.4 2.3.6 3.6.6.6 0 1 .4 1 1V20c0 .6-.4 1-1 1A17 17 0 0 1 3 4c0-.6.4-1 1-1h3.5c.6 0 1 .4 1 1 0 1.3.2 2.5.6 3.6.1.3 0 .7-.2 1z"/></svg>
    0400 123 456
  </div>
  <span class="nav-mark abs"></span>
  <nav class="main-nav abs">
    <a href="#">About Us</a><a href="#">Our Service</a><a href="#">Our Project</a><a href="#">Testimonials</a><a href="#">Contact Us</a>
  </nav>
</header>

<section class="hero">
  <div class="hero-photo abs" role="img" aria-label="Bright industrial warehouse interior with ceiling lights and a yellow forklift on the right"></div>
  <div class="hero-tag abs">We Are Specialized in Electrical Services</div>
</section>

<section class="feature-panel abs"></section>
<div class="feature abs" style="left:120px;top:690px">
  <div class="ring"><div class="core">
    <svg width="50" height="56" viewBox="0 0 50 56"><circle cx="25" cy="20" r="15" fill="none" stroke="#fff" stroke-width="4"/><path d="M15 32 10 54l15-8 15 8-5-22" fill="none" stroke="#fff" stroke-width="4"/></svg>
  </div></div>
  <h3>Satisfaction<br>Guarantee</h3>
</div>
<div class="feature abs" style="left:368px;top:690px">
  <div class="ring"><div class="core">
    <svg width="60" height="44" viewBox="0 0 60 44"><path d="M8 34a22 22 0 0 1 44 0z" fill="#fff"/><rect x="2" y="34" width="56" height="6" rx="3" fill="#fff"/><rect x="27" y="6" width="6" height="16" fill="#3a3a3a"/></svg>
  </div></div>
  <h3>Safety</h3>
</div>
<div class="feature abs" style="left:620px;top:690px">
  <div class="ring"><div class="core">
    <svg width="50" height="56" viewBox="0 0 50 56"><circle cx="25" cy="22" r="18" fill="#fff"/><circle cx="25" cy="22" r="9" fill="#3a3a3a"/><path d="M14 36 10 54l15-7 15 7-4-18" fill="#fff"/></svg>
  </div></div>
  <h3>Quality</h3>
</div>
<div class="feature abs" style="left:880px;top:690px">
  <div class="ring"><div class="core">
    <svg width="50" height="50" viewBox="0 0 50 50"><rect x="4" y="22" width="10" height="24" fill="#fff"/><path d="M18 22 28 4c4 0 6 3 5 7l-2 9h12c3 0 5 3 4 6l-4 16c-1 3-3 4-6 4H18z" fill="#fff"/></svg>
  </div></div>
  <h3>Reliability</h3>
</div>

<section class="about abs" style="left:130px;top:915px;width:940px">
  <h2>About <span class="accent">Tolbran Engineering</span></h2>
  <p>Our licensed team delivers safe, reliable electrical work for commercial and industrial sites across the region. From new installations and switchboard upgrades to maintenance, testing and fault finding, every project is planned carefully, completed on time and backed by clear communication. We support government, mining and private clients with practical solutions that keep operations running smoothly and fully compliant.</p>
</section>

<h2 class="section-title abs" style="top:1130px">Our <span class="accent">Services</span></h2>
<svg class="slider-arrow abs" style="left:68px" viewBox="0 0 20 30"><path d="M15 3 4 15l11 12" fill="none" stroke="#999" stroke-width="3"/></svg>
<svg class="slider-arrow abs" style="left:1112px" viewBox="0 0 20 30"><path d="m5 3 11 12L5 27" fill="none" stroke="#999" stroke-width="3"/></svg>
<article class="service-card dark abs" style="left:100px" role="img" aria-label="Residential electrical work photo">
  <h3>Residential</h3>
  <p>Safe wiring, lighting and power upgrades for homes, installed neatly by licensed electricians.</p>
  <span class="btn">Read More ›</span>
</article>
<article class="service-card active abs" style="left:437px" role="img" aria-label="Commercial electrical work photo">
  <h3>Commercial</h3>
  <p>Fit-outs, data cabling and maintenance for offices, retail and public buildings of all sizes.</p>
  <span class="btn">Read More ›</span>
</article>
<article class="service-card dark abs" style="left:774px" role="img" aria-label="Industrial electrical work photo">
  <h3>Industrial</h3>
  <p>Plant installations, switchboards and testing for mining, factory and heavy industry sites.</p>
  <span class="btn">Read More ›</span>
</article>

<h2 class="section-title abs" style="top:1590px">Recent <span class="accent">Projects</span></h2>
<p class="section-sub abs" style="top:1648px">A selection of recent installations completed for our commercial and industrial clients.</p>
<div class="project feature-tile abs" style="left:100px;top:1700px;width:260px;height:332px">
  <div class="plus"><svg width="22" height="22" viewBox="0 0 22 22"><path d="M11 2v18M2 11h18" stroke="#f37122" stroke-width="3"/></svg></div>
  <span>Volta Blockline 3000</span>
</div>
<div class="project abs" style="left:372px;top:1700px;width:236px;height:160px" role="img" aria-label="Warehouse lighting installation"></div>
<div class="project abs" style="left:620px;top:1700px;width:232px;height:160px" role="img" aria-label="Factory floor with overhead lights"></div>
<div class="project abs" style="left:868px;top:1700px;width:232px;height:160px" role="img" aria-label="Large industrial hall interior"></div>
<div class="project abs" style="left:372px;top:1872px;width:236px;height:160px" role="img" aria-label="Electrical cabinet fit-out"></div>
<div class="project abs" style="left:620px;top:1872px;width:232px;height:160px;background:linear-gradient(160deg,#e0a45a,#8a5a2a)" role="img" aria-label="Multimeter testing on a circuit"></div>
<div class="project abs" style="left:868px;top:1872px;width:232px;height:160px" role="img" aria-label="Electrician working on a switchboard"></div>

<section class="partners abs" style="left:100px;top:2065px">
  <h2 class="col-title">Our <span class="accent">Partners</span></h2>
  <p>We work alongside trusted suppliers and contractors who share our commitment to quality, safety and reliable service on every job.</p>
</section>
<div class="partner-badge abs" style="left:110px;top:2180px"></div>
<div class="partner-badge abs" style="left:270px;top:2180px"></div>
<div class="partner-badge round abs" style="left:450px;top:2178px"></div>
<div class="partner-badge abs" style="left:110px;top:2300px"></div>
<div class="partner-badge round abs" style="left:287px;top:2298px"></div>
<div class="partner-badge abs" style="left:430px;top:2300px"></div>

<h2 class="col-title abs" style="left:640px;top:2065px">Quick <span class="accent">Inquiry</span></h2>
<div class="form-field abs" style="top:2125px">Your Name</div>
<div class="form-field abs" style="top:2177px">Email</div>
<div class="form-field abs" style="top:2229px">Your Website</div>
<div class="form-field abs" style="top:2281px;height:90px">Message</div>
<div class="submit abs">Submit ›</div>

<footer class="site-footer abs">
  <div class="foot-col abs" style="left:100px;top:40px">
    <h4>Quick <span class="accent">Links</span></h4>
    <ul><li>› Home</li><li>› About Us</li><li>› Our Services</li><li>› Our Project</li><li>› Testimonials</li><li>› Contact Us</li></ul>
  </div>
  <div class="foot-col abs" style="left:280px;top:40px;width:270px">
    <h4>Contact <span class="accent">Information</span></h4>
    <div class="row" style="margin-top:14px">
      <svg width="12" height="16" viewBox="0 0 12 16" style="margin-top:4px"><path d="M6 0a6 6 0 0 0-6 6c0 4.5 6 10 6 10s6-5.5 6-10a6 6 0 0 0-6-6zm0 8.5A2.5 2.5 0 1 1 6 3.5a2.5 2.5 0 0 1 0 5z" fill="#f37122"/></svg>
      <div><span class="accent">Tolbran Engineering</span><br>Hillmoor, Western Australia<br>6099</div>
    </div>
    <div class="row" style="margin-top:8px"><svg width="12" height="12" viewBox="0 0 24 24" style="margin-top:5px"><path fill="#f37122" d="M6.6 10.8a15 15 0 0 0 6.6 6.6l2.2-2.2c.3-.3.7-.4 1-.2 1.1.4 2.3.6 3.6.6.6 0 1 .4 1 1V20c0 .6-.4 1-1 1A17 17 0 0 1 3 4c0-.6.4-1 1-1h3.5c.6 0 1 .4 1 1 0 1.3.2 2.5.6 3.6.1.3 0 .7-.2 1z"/></svg>0400 123 456</div>
    <div class="row"><svg width="12" height="12" viewBox="0 0 24 24" style="margin-top:5px"><path fill="#f37122" d="M2 5h20v14H2zm2 2v.5l8 5 8-5V7z"/></svg>0400 123 457</div>
    <div class="row"><svg width="12" height="12" viewBox="0 0 24 24" style="margin-top:5px"><path fill="#f37122" d="M2 5h20v14H2zm2 2v.5l8 5 8-5V7z"/></svg>info@tolbran.net.au</div>
  </div>
  <div class="foot-col abs" style="left:580px;top:40px">
    <h4>Location <span class="accent">Map</span></h4>
    <div class="map-area" role="img" aria-label="Street map showing the business location"></div>
  </div>
  <div class="abs" style="left:930px;top:40px">
    <div class="foot-brand"><span class="dot"></span><div><div class="foot-brand-name">TOLBRAN</div><div class="foot-brand-ec">EC 012345</div></div></div>
    <div class="member-badge"></div>
  </div>
</footer>
<div class="copyright abs">Copyright © 2016 Tolbran Engineering. All Rights Reserved.</div>
<div class="social abs"><span></span><span></span><span></span><span></span></div>

</body>
</html>
```